8 x 8 Social Media Design - Crest Pathway #1

Why be a regular Agent, when you can be a Boss?
MOVA PRIMEHOLD REALTY GROUP
We offer Four Levels of Participation
You Increase your Earning Potential at Each Level
Level One - Learn to Earn Additional Income Through....
Mortgage Originations - Dual Licensing / No Additional Work
Real Estate Investing - Invest Jointly with Us
Agent Recruitment - Up to 10% Override
Level Two - Team Leader
Level Three - Minority Mova Franchise Ownership
Level Four - Majority Mova Franchise Ownership
For more information visit us at www.careersatmovaprmhold.example and request a meeting with our Managing Broker, Mr. Harold Tismeer.

```html
<!DOCTYPE html>
<html lang="en">
<head>
<meta charset="utf-8">
<title>Crest Pathway – Be a Boss</title>
<link rel="stylesheet" href="https://fonts.googleapis.com/css2?family=Montserrat:wght@600;700;800;900&family=Open+Sans:wght@400;600;700;800&display=swap">
<style>
  :root {
    --ink: #111111;
    --white: #ffffff;
    --gold: #b8900f;
    --gold-light: #f2c832;
    --gold-dark: #8f6a08;
    --yellow: #f7d11e;
    --teal: #17969a;
    --money-light: #eef0ec;
    --money-mid: #cfd6cc;
    --coat: #1d1f22;
    --coat-light: #3a3d42;
  }
  html, body {
    margin: 0;
    padding: 0;
    width: 1200px;
    height: 1200px;
    overflow: hidden;
    background: var(--white);
  }
  .poster {
    display: block;
    width: 1200px;
    height: 1200px;
  }
  .headline { font-family: "Montserrat", sans-serif; font-weight: 800; font-size: 45px; }
  .headline-dark { fill: var(--ink); }
  .headline-gold { fill: var(--gold); }
  .hero { font-family: "Montserrat", sans-serif; font-weight: 900; }
  .hero-be { fill: var(--ink); font-size: 200px; }
  .hero-gold { fill: url(#goldFoil); }
  .offer-tag { font-family: "Montserrat", sans-serif; font-weight: 800; font-size: 26px; fill: var(--white); }
  .offer-text { font-family: "Montserrat", sans-serif; font-weight: 800; font-size: 32px; fill: var(--ink); }
  .earning-note { font-family: "Montserrat", sans-serif; font-weight: 800; font-size: 31px; fill: var(--ink); }
  .level-label { font-family: "Montserrat", sans-serif; font-weight: 800; font-size: 46px; fill: var(--ink); }
  .level-desc { font-family: "Open Sans", sans-serif; font-weight: 700; font-size: 23px; fill: var(--white); }
  .income-intro { font-family: "Open Sans", sans-serif; font-weight: 600; font-size: 21px; fill: var(--white); }
  .income-item { font-family: "Open Sans", sans-serif; font-weight: 400; font-size: 21px; fill: var(--white); }
  .income-key { font-weight: 800; fill: var(--yellow); }
  .brand-name { font-family: "Montserrat", sans-serif; font-weight: 900; font-size: 66px; fill: var(--teal); }
  .brand-group { font-family: "Montserrat", sans-serif; font-weight: 700; font-size: 13.5px; fill: var(--ink); }
  .contact { font-family: "Open Sans", sans-serif; font-weight: 600; font-size: 21px; fill: var(--ink); }
  .contact-strong { font-weight: 800; }
  .contact-url { font-family: "Open Sans", sans-serif; font-weight: 700; font-size: 20px; fill: var(--white); }
</style>
</head>
<body>
<svg class="poster" viewBox="0 0 1200 1200" xmlns="http://www.w3.org/2000/svg">
  <defs>
    <linearGradient id="goldFoil" x1="0" y1="0" x2="1" y2="1">
      <stop offset="0" stop-color="#f5d35a"/>
      <stop offset="0.35" stop-color="#c99a16"/>
      <stop offset="0.6" stop-color="#e8bd35"/>
      <stop offset="1" stop-color="#8f6a08"/>
    </linearGradient>
    <linearGradient id="levelGold" x1="0" y1="0" x2="0" y2="1">
      <stop offset="0" stop-color="#ffe04a"/>
      <stop offset="1" stop-color="#e3b40e"/>
    </linearGradient>
    <linearGradient id="moneyTone" x1="0" y1="0" x2="1" y2="1">
      <stop offset="0" stop-color="var(--money-light)"/>
      <stop offset="0.5" stop-color="var(--money-mid)"/>
      <stop offset="1" stop-color="var(--money-light)"/>
    </linearGradient>
    <linearGradient id="coatTone" x1="0" y1="0" x2="0" y2="1">
      <stop offset="0" stop-color="var(--coat-light)"/>
      <stop offset="1" stop-color="var(--coat)"/>
    </linearGradient>
    <linearGradient id="portraitTone" x1="0" y1="0" x2="0" y2="1">
      <stop offset="0" stop-color="#b9b2a8"/>
      <stop offset="1" stop-color="#4a3a30"/>
    </linearGradient>
  </defs>

  <!-- header band -->
  <rect class="header-band" x="0" y="0" width="1200" height="90" fill="var(--white)"/>
  <text class="headline" x="600" y="66" text-anchor="middle">
    <tspan class="headline-dark">WHY BE A REGULAR AGENT, </tspan><tspan class="headline-gold">WHEN YOU CAN</tspan>
  </text>

  <!-- cash backdrop -->
  <rect class="cash-backdrop" x="0" y="90" width="1200" height="560" fill="url(#moneyTone)" role="img" aria-label="Background of stacked dollar bills"/>

  <!-- yellow wedge and black base -->
  <polygon class="yellow-wedge" points="0,421 555,671 0,869" fill="var(--yellow)"/>
  <polygon class="black-base" points="0,869 1200,440 1200,1200 0,1200" fill="var(--ink)"/>

  <!-- featured agent photo -->
  <rect class="agent-photo" x="440" y="118" width="360" height="630" rx="60" fill="url(#coatTone)" role="img" aria-label="Photo of a smiling agent in a black hat, glasses and dark coat, seated"/>

  <!-- hero words -->
  <text class="hero hero-be" x="48" y="312" textLength="212" lengthAdjust="spacingAndGlyphs">BE</text>
  <text class="hero hero-gold" x="352" y="282" font-size="210" textLength="128" lengthAdjust="spacingAndGlyphs">A</text>
  <text class="hero hero-gold" x="196" y="488" font-size="215" textLength="538" lengthAdjust="spacingAndGlyphs">BOSS</text>

  <!-- offer block -->
  <text class="hero hero-gold" x="808" y="316" font-size="185" textLength="100" lengthAdjust="spacingAndGlyphs">4</text>
  <rect class="offer-tag-box" x="916" y="185" width="180" height="36" fill="var(--ink)"/>
  <text class="offer-tag" x="1006" y="213" text-anchor="middle">WE OFFER</text>
  <text class="offer-text" x="920" y="263">LEVELS OF</text>
  <text class="offer-text" x="920" y="304">PARTICIPATION</text>

  <!-- earning note -->
  <text class="earning-note">
    <tspan x="29" y="606">YOU</tspan>
    <tspan x="29" y="644">INCREASE</tspan>
    <tspan x="29" y="682">YOUR EARNING</tspan>
    <tspan x="29" y="720">POTENTIAL AT</tspan>
    <tspan x="29" y="758">EACH LEVEL</tspan>
  </text>

  <!-- growth arrow -->
  <polyline class="growth-arrow" points="199,584 445,745 1130,486" fill="none" stroke="var(--teal)" stroke-width="16" stroke-linejoin="miter"/>
  <polygon class="growth-arrow-head" points="1182,466 1110,462 1132,512" fill="var(--teal)"/>

  <!-- level ladder -->
  <g class="level-ladder" transform="translate(40 970) rotate(-20.1)">
    <rect x="0" y="-36" width="1260" height="72" fill="url(#levelGold)"/>
    <rect x="286" y="-36" width="10" height="72" fill="var(--ink)"/>
    <rect x="582" y="-36" width="10" height="72" fill="var(--ink)"/>
    <rect x="886" y="-36" width="10" height="72" fill="var(--ink)"/>
    <text class="level-label" x="143" y="16" text-anchor="middle">LEVEL 1</text>
    <text class="level-label" x="439" y="16" text-anchor="middle">LEVEL 2</text>
    <text class="level-label" x="739" y="16" text-anchor="middle">LEVEL 3</text>
    <text class="level-label" x="1040" y="16" text-anchor="middle">LEVEL 4</text>
  </g>

  <!-- level descriptions -->
  <text class="level-desc" x="570" y="934">TEAM LEADER</text>
  <text class="level-desc">
    <tspan x="652" y="817">MINORITY MOVA</tspan>
    <tspan x="652" y="846">FRANCHISE</tspan>
    <tspan x="652" y="875">OWNERSHIP</tspan>
  </text>
  <text class="level-desc">
    <tspan x="938" y="708">MAJORITY MOVA</tspan>
    <tspan x="938" y="737">FRANCHISE</tspan>
    <tspan x="938" y="766">OWNERSHIP</tspan>
  </text>

  <!-- extra income list -->
  <text class="income-intro" x="43" y="1054">Learn to Earn Additional Income Through....</text>
  <text class="income-item">
    <tspan x="43" y="1082"><tspan class="income-key">• MORTGAGE ORIGINATIONS</tspan> -</tspan>
    <tspan x="62" y="1108">Dual Licensing / No Additional Work</tspan>
    <tspan x="43" y="1134"><tspan class="income-key">• REAL ESTATE INVESTING</tspan> - Invest Jointly with Us</tspan>
    <tspan x="43" y="1161"><tspan class="income-key">• AGENT RECRUITMENT</tspan> - Up to 10% Override</tspan>
  </text>

  <!-- contact panel -->
  <polygon class="contact-panel" points="752,934 1200,934 1200,1200 676,1200" fill="var(--white)"/>
  <circle class="broker-ring" cx="1084" cy="966" r="104" fill="var(--gold-light)"/>
  <circle class="broker-photo" cx="1084" cy="966" r="94" fill="url(#portraitTone)" role="img" aria-label="Portrait photo of the managing broker"/>

  <text class="brand-name" x="870" y="1028" text-anchor="middle">MOVA</text>
  <text class="brand-group" x="870" y="1056" text-anchor="middle">MOVA PRIMEHOLD REALTY GROUP</text>

  <text class="contact" x="955" y="1094" text-anchor="middle">For more information visit us at</text>
  <rect class="contact-url-pill" x="746" y="1106" width="412" height="34" rx="17" fill="var(--teal)"/>
  <text class="contact-url" x="952" y="1130" text-anchor="middle">www.careersatmovaprmhold.example</text>
  <text class="contact" x="955" y="1163" text-anchor="middle">and request a meeting with our</text>
  <text class="contact contact-strong" x="955" y="1189" text-anchor="middle">Managing Broker, Mr. Harold Tismeer.</text>
</svg>
</body>
</html>
```